Gutschein-Design für Bauträgerfirma
Zielgruppe
Wir sind eine Bauträgerfirma und verkaufen Wohnungen für die gehobene Klasse.
Aufgabenstellung
Auflösung min. 150dpi, Format: 3,56m x 2,52m,
Dieses Banner soll eine Werbung bzw. einen Gutschein enthalten.
Folgender Text soll enthalten sein: Wenn Sie eine Wohnung bis zum 31.12.2018 bei uns kaufen, erhalten Sie einen Bemusterungsgutschein von 5.000€.
Der Text kann natürlich auch anders formuliert werden, der Kern sollte erhalten bleiben.
Die Unterlagen können auch im anderen Format zur Verfügung gestellt werden. Es sind alle Render in großem Format verfügbar.

```html
<!DOCTYPE html>
<html lang="de">
<head>
<meta charset="utf-8">
<title>Wohnresidenz am Lindenhof – Banner</title>
<link rel="stylesheet" href="https://fonts.googleapis.com/css2?family=Montserrat:wght@500&family=Open+Sans:ital,wght@0,400;0,600;1,400;1,600&display=swap">
<style>
  :root {
    --page: #e6e6e6;
    --navy: #1c2d52;
    --panel: #28406f;
    --white: #ffffff;
    --text-light: #e9eef7;
    --photo-sky: #9fb8cf;
    --photo-lawn: #5f8a3e;
    --photo-interior: #d9d6d0;
  }
  * { margin: 0; padding: 0; box-sizing: border-box; }
  html, body { width: 1130px; height: 1200px; overflow: hidden; }
  body { background: var(--page); font-family: "Open Sans", Arial, sans-serif; position: relative; }

  .banner {
    position: absolute; left: 40px; top: 232px;
    width: 1050px; height: 736px;
    background: var(--navy);
  }
  .title-box {
    position: absolute; left: 378px; top: 53px; width: 606px; height: 72px;
    background: var(--white);
    display: flex; align-items: center; justify-content: center;
    z-index: 2;
  }
  .title-box h1 {
    font-family: "Montserrat", Arial, sans-serif; font-weight: 500;
    font-size: 31px; letter-spacing: 1px; color: var(--navy);
  }
  .photo { position: absolute; }
  .photo-exterior {
    left: 0; top: 92px; width: 525px; height: 403px;
    background: linear-gradient(180deg, var(--photo-sky) 0%, #c9d6e0 45%, #e8e8e6 60%, var(--photo-lawn) 82%, #4a6f2f 100%);
  }
  .photo-kitchen {
    left: 0; top: 509px; width: 267px; height: 145px;
    background: linear-gradient(135deg, #eeece8 0%, var(--photo-interior) 55%, #8c8f93 100%);
  }
  .photo-living {
    left: 281px; top: 509px; width: 245px; height: 145px;
    background: linear-gradient(135deg, #f1efea 0%, var(--photo-interior) 50%, #a38b6e 100%);
  }
  .info-panel {
    position: absolute; left: 539px; top: 147px; width: 506px; height: 403px;
    background: var(--panel);
    padding: 42px 40px 0 40px;
    color: var(--text-light);
  }
  .info-panel h2 {
    font-size: 25px; line-height: 34px; font-weight: 600;
    color: var(--white); margin-bottom: 40px;
  }
  .features { list-style: none; }
  .features li {
    font-size: 17.5px; line-height: 28px; padding-left: 20px; position: relative;
  }
  .features li::before { content: "•"; position: absolute; left: 0; }
  .voucher-box {
    position: absolute; left: 578px; top: 503px; width: 440px; height: 117px;
    background: var(--white); color: var(--navy);
    display: flex; align-items: center; justify-content: center; text-align: center;
    font-style: italic; font-size: 16.5px; line-height: 26px;
    z-index: 2;
  }
  .footer {
    position: absolute; left: 124px; top: 686px;
    color: var(--white); font-size: 21px; line-height: 30px; letter-spacing: 0.5px;
  }
  .brand {
    position: absolute; left: 790px; top: 690px;
    display: flex; align-items: center; gap: 10px;
    color: var(--white); font-size: 17px; line-height: 22px; font-weight: 600;
    letter-spacing: 1px;
  }
  .brand-square { width: 12px; height: 12px; background: var(--white); }
</style>
</head>
<body>
  <section class="banner">
    <div class="title-box"><h1>WOHNRESIDENZ AM LINDENHOF</h1></div>

    <div class="photo photo-exterior" role="img" aria-label="Rendering der modernen Wohnanlage mit Terrassen und Rasenfläche"></div>
    <div class="photo photo-kitchen" role="img" aria-label="Rendering einer hellen Küche"></div>
    <div class="photo photo-living" role="img" aria-label="Rendering eines Wohnbereichs mit Küchenzeile"></div>

    <div class="info-panel">
      <h2>Wohnen zum Wohlfühlen.</h2>
      <ul class="features">
        <li>19 Wohnungen , 2 bis 4 Zimmern , ca. 60 bis 160 Quadratmeter</li>
        <li>helle, freundliche und barrierefreie Bauweise</li>
        <li>besonders energieeffiziente KfW55 Häusern mit Blockheizkraftwerk</li>
        <li>attraktiver Spielplatz auf dem Gelände und Tiefgarage ...</li>
      </ul>
    </div>

    <div class="voucher-box">
      <p>Kaufen Sie eine Wohnung bis zum <strong>31.12.2018</strong>,<br>bedanken wir uns mit einem<br>Bemusterungsgutschein im Wert von <strong>5.000 €</strong>.</p>
    </div>

    <p class="footer">WWW.HALDEN-IMMOBILIEN.COM | TEL. 0 12 34 - 567 89 00</p>

    <div class="brand">
      <span class="brand-square"></span>
      <span class="brand-name">HALDEN IMMOBILIEN</span>
    </div>
  </section>
</body>
</html>
```